Massage therapist LMT

I need something simple and beautiful I'm a man no flowers, no leafs,no tree please

Target Market(s)

People who suffer ( body pain,stess,body injury ect.. )

Industry/Entity Type

Massage Therapy

Contact Information for Business Card

Marcus T Abernathy LMT

Font styles to use
Serif
Script

Colors

Designer to choose colors to be used in the design.

Requirements
Must have
• Get a massage
• For the
• Health
• Of it
Nice to have
• Skeleton
Should not have
• No flowers
• No tree

```html
<!DOCTYPE html>
<html lang="en">
<head>
<meta charset="utf-8">
<title>Marcus T Abernathy LMT – Business Card</title>
<link href="https://fonts.googleapis.com/css2?family=Noto+Serif&family=Tinos&family=Great+Vibes&display=swap" rel="stylesheet">
<style>
  :root {
    --page-bg: #1e1e20;
    --card-black: #1b1b1d;
    --card-black-curve: #262628;
    --card-grey: #2c2c2e;
    --blue-deep: #1f2c8e;
    --blue-mid: #3442b4;
    --blue-light: #5a6fd0;
    --text-white: #f2f2f2;
    --phone-blue: #4a5fd0;
    --bone: #c9c9c9;
  }
  * { margin: 0; padding: 0; box-sizing: border-box; }
  html, body {
    width: 1200px; height: 1101px; overflow: hidden;
    background: var(--page-bg);
  }
  .canvas { position: relative; width: 1200px; height: 1101px; }

  .card {
    position: absolute;
    width: 620px; height: 354px;
    overflow: hidden;
    border-radius: 3px;
  }
  .card-back { left: 110px; top: 120px; background: var(--card-black); }
  .card-front { left: 470px; top: 620px; background: var(--card-grey); }
  .card svg.card-shapes { position: absolute; inset: 0; }

  .skeleton-art {
    position: absolute; left: 70px; top: 30px;
    width: 140px; height: 300px;
    border-radius: 60px 60px 20px 20px;
    background: radial-gradient(ellipse at center, #8a8a8a 0%, #4a4a4c 55%, var(--card-black) 100%);
  }
  .motto {
    position: absolute; left: 225px; top: 44px;
    list-style: none;
    font-family: "Noto Serif", serif;
    font-size: 33px; color: var(--text-white);
    text-shadow: 0 0 6px rgba(255,255,255,0.35);
  }
  .motto li { line-height: 64px; }

  .figure-art {
    position: absolute; left: 40px; top: 40px;
    width: 250px; height: 314px;
    border-radius: 90px 90px 0 0;
    background: radial-gradient(ellipse at 50% 40%, #b8c4f2 0%, #6474d4 45%, rgba(52,66,180,0) 80%);
  }
  .therapist-name {
    position: absolute; right: 24px; top: 66px;
    font-family: "Great Vibes", cursive;
    font-weight: 400;
    font-size: 38px; color: var(--text-white);
    white-space: nowrap;
    text-shadow: 0 0 8px rgba(255,255,255,0.5);
  }
  .contact {
    position: absolute; right: 26px; top: 222px;
    text-align: right;
    font-family: "Tinos", serif;
    color: var(--text-white);
  }
  .contact .phone { font-size: 31px; color: var(--phone-blue); line-height: 40px; }
  .contact .web, .contact .area { font-size: 21px; line-height: 27px; }
</style>
</head>
<body>
<main class="canvas">

  <section class="card card-back">
    <svg class="card-shapes" width="620" height="354" viewBox="0 0 620 354">
      <path d="M0 354 C 220 260 420 120 620 0 L620 354 Z" fill="var(--card-black-curve)" opacity="0.6"/>
      <path d="M250 0 C 470 40 560 200 520 354" fill="none" stroke="#333336" stroke-width="2"/>
    </svg>
    <div class="skeleton-art" role="img" aria-label="Illustration of a full human skeleton"></div>
    <ul class="motto">
      <li>- Get a massage</li>
      <li>- For the</li>
      <li>- Health</li>
      <li>- Of it</li>
    </ul>
  </section>

  <section class="card card-front">
    <svg class="card-shapes" width="620" height="354" viewBox="0 0 620 354">
      <defs>
        <linearGradient id="blue-field" x1="0" y1="0" x2="1" y2="0.4">
          <stop offset="0" stop-color="var(--blue-deep)"/>
          <stop offset="0.6" stop-color="var(--blue-mid)"/>
          <stop offset="1" stop-color="var(--blue-light)"/>
        </linearGradient>
      </defs>
      <path d="M0 0 H620 V100 C 470 210 280 280 0 300 Z" fill="url(#blue-field)"/>
      <path d="M210 0 C 330 50 400 120 420 200" fill="none" stroke="#8c9be6" stroke-width="1.5" opacity="0.7"/>
      <path d="M330 0 C 420 50 460 110 470 170" fill="none" stroke="#7e8edf" stroke-width="1" opacity="0.5"/>
    </svg>
    <div class="figure-art" role="img" aria-label="Glowing blue x-ray style illustration of a male body with energy swirls"></div>
    <h1 class="therapist-name">Marcus T Abernathy LMT</h1>
    <div class="contact">
      <p class="phone">555.014.2387</p>
      <p class="web">www.abernathylmt.com</p>
      <p class="area">Riverton, TN &amp; Oakdale, TN</p>
    </div>
  </section>

</main>
</body>
</html>
```